Wellness Coach needs a Business Card

I need a business card for a start-up coaching business called Brightfern Vitality Partners. I don't have a logo as such but I am looking to have a web page created in a few months time and hopefully the person who designs this card will be able to do or help with the web project. This business card will be used primarily for networking and for initial clients.

As the name implies, the coaching focus is wide-ranging and includes multiple facets of health and wellness, including physical, mental, spiritual, etc. I am a Personal Trainer so the main focus will be physical training, but with the other areas of life / wellness included.

My information for the card:

Dorian Pleshey
Director
Brightfern Vitality Partners

Phone: 0413 862051
Address: PO Box 514 Mitchell ACT 2911
email: dorian@brightfernvitalitypartners.com.au
web: http://www.brightfernvitalitypartners.com.au

Target Market(s)

People wanting to change their life by getting fit and by addressing issues in their lives that are holding them back. I will target people already into fitness but who want to extend their approach into life coaching.

Industry/Entity Type

Health

Requirements
Must have
• - I am keen on a single sided business card design but if your design lends itself to a double sided design then I'm open to that thanks.

- I love the idea of fresh - something that represents the awakening of somebody who has been dormant. Lime green strikes me as fresh, but this is just an idea, not mandatory.
Nice to have
• - I'm keen for minimisation but I don't mind an image in the background taking up the whole space, as long as it is not too busy.

- Two types of images that I can visualise are a mountain summit or a path leading into nature or up a mountain - an adventure! Again, not mandatory, just an idea.
Should not have
• - I'm not keen on over-crowding.
- One image I'm not keen on is someone standing on top of a mountain with their arms in the air - too cliché.

```html
<!DOCTYPE html>
<html lang="en">
<head>
<meta charset="utf-8">
<title>Brightfern Vitality Partners – Business Card</title>
<link rel="stylesheet" href="https://fonts.googleapis.com/css2?family=Questrial&family=Mulish:wght@400;500&display=swap">
<style>
  :root {
    --lime: #b8ff00;
    --ink: #111111;
    --paper: #ffffff;
    --leaf-dark: #0a0a0a;
    --leaf-mid: #2b2b2b;
  }
  html, body {
    margin: 0;
    padding: 0;
    width: 1200px;
    height: 777px;
    overflow: hidden;
    background: var(--paper);
  }
  .card {
    position: relative;
    width: 1200px;
    height: 777px;
    background: var(--paper);
    color: var(--ink);
    overflow: hidden;
  }
  .card__waves {
    position: absolute;
    inset: 0;
    width: 1200px;
    height: 777px;
  }
  .card__waves .wave { fill: var(--lime); }
  .card__foliage {
    position: absolute;
    left: 922px;
    top: 0;
    width: 262px;
    height: 316px;
    border-radius: 0 0 30% 55% / 0 0 20% 40%;
    background: radial-gradient(ellipse at 55% 40%, var(--leaf-mid), var(--leaf-dark) 70%);
  }
  .identity {
    position: absolute;
    left: 0;
    right: 0;
    text-align: center;
  }
  .identity__name {
    top: 256px;
    margin: 0;
    font-family: "Questrial", sans-serif;
    font-weight: 400;
    font-size: 66px;
    letter-spacing: 0.06em;
    line-height: 1;
  }
  .identity__role {
    top: 334px;
    font-family: "Questrial", sans-serif;
    font-size: 37px;
    letter-spacing: 0.1em;
    line-height: 1;
  }
  .identity__company {
    top: 386px;
    font-family: "Mulish", sans-serif;
    font-weight: 400;
    font-size: 52px;
    letter-spacing: -0.01em;
    line-height: 1;
  }
  .identity__phone {
    top: 464px;
    display: flex;
    justify-content: center;
    align-items: center;
    gap: 10px;
    font-family: "Mulish", sans-serif;
    font-size: 39px;
    line-height: 1;
  }
  .identity__phone svg { width: 56px; height: 38px; }
  .identity__phone .icon { fill: var(--lime); }
  .contact {
    position: absolute;
    left: 32px;
    top: 632px;
    margin: 0;
    padding: 0;
    list-style: none;
    font-family: "Mulish", sans-serif;
    font-size: 33px;
    line-height: 35px;
    color: var(--ink);
  }
  .contact li:nth-child(2) { margin-left: -3px; }
</style>
</head>
<body>
  <div class="card">
    <svg class="card__waves" viewBox="0 0 1004 650" preserveAspectRatio="none" aria-hidden="true">
      <path class="wave wave--top" d="M0,0 H1004 V70 C985,160 920,215 820,205 C700,192 600,120 470,55 C360,5 220,5 120,35 C60,55 20,90 0,120 Z"/>
      <path class="wave wave--bottom" d="M0,650 V525 C70,455 200,430 330,440 C480,452 620,500 760,535 C880,565 960,570 1004,540 V650 Z"/>
    </svg>

    <div class="card__foliage" role="img" aria-label="Cluster of dark stylised leaves sweeping down from the top right corner"></div>

    <h1 class="identity identity__name">DORIAN PLESHEY</h1>
    <div class="identity identity__role">DIRECTOR</div>
    <div class="identity identity__company">Brightfern Vitality Partners</div>
    <div class="identity identity__phone">
      <svg viewBox="0 0 56 38" aria-hidden="true">
        <path class="icon" d="M4,14 C4,6 16,2 28,2 C40,2 52,6 52,14 L52,18 L41,18 L41,12 L15,12 L15,18 L4,18 Z"/>
        <path class="icon" d="M17,15 H39 L47,28 V36 H9 V28 Z"/>
        <circle cx="28" cy="27" r="5" fill="#ffffff"/>
      </svg>
      <span>0413 862051</span>
    </div>

    <ul class="contact">
      <li>address: PO Box 514 Larkfield ACT 2914</li>
      <li>email: dorian@brightfernvitalitypartners.com.au</li>
      <li>web: http://www.brightfernvitalitypartners.com.au</li>
    </ul>
  </div>
</body>
</html>
```